Brisk Hounds Dog Behaviour, Training and Natural Healthcare Business Card Design

I am an experienced and qualified dog behavioural trainer and natural animal healthcare consultant offering a range of services to help pet dog owners with the "whole dog".
COLOURS: A soft light blue in the background - can be fading out or split, red should also feature
LOGO: Dog, healing hands, silhouette, shadow
SERVICES: Behaviour Consults, Training, Complex Skills Coaching Walking Coaching, Diet & Nutrition, Environmental Enrichment, Lifestyle and Lifestage Adaptations, Massage, Natural Health Options
BY LINE: Happy Dogs, Happy Owners
VALUES: Promoting communication and connection between dogs and their owners.
FOCUS: Nutritional guidance and environmental adaptation are often needed to complete the package and increase the success rate of training and behaviour modification.

Target Market(s)

Everyone who has a dog who they wish to improve their relationship with

Industry/Entity Type

Communication

Contact Information for Business Card

Brisk Hounds, Renata Walcott, 0472 680351, briskhounds7@mailnest.example, www.briskhounds7.example, Qualified Dog Behavioural Trainer and Natural Animal Healthcare Consultant

Font styles to use
Sans Serif
Script

Colors
85cae6
ec2027

Requirements
Must have
• A clear indication that it is a dog services business. A raised feature
Should not have
• Pawprints, cartoons

```html
<!DOCTYPE html>
<html lang="en">
<head>
<meta charset="utf-8">
<title>Brisk Hounds — Business Card</title>
<link rel="stylesheet" href="https://fonts.googleapis.com/css2?family=Arimo:ital,wght@0,400;0,700;1,700&display=swap">
<style>
  :root {
    --ink: #000000;
    --white: #ffffff;
    --sky: #2aa8e0;
    --sky-soft: #85cae6;
    --sky-pale: #d8eef9;
    --silhouette-tone: #111111;
  }
  html, body {
    margin: 0;
    padding: 0;
    width: 1200px;
    height: 720px;
    overflow: hidden;
    background: var(--white);
  }
  .card {
    position: relative;
    width: 1200px;
    height: 720px;
    overflow: hidden;
    background: var(--white);
    font-family: "Arimo", Arial, sans-serif;
    color: var(--ink);
  }
  .card-backdrop {
    position: absolute;
    inset: 0;
    width: 1200px;
    height: 720px;
  }
  .brand-name {
    position: absolute;
    left: 0;
    right: 0;
    top: 22px;
    margin: 0;
    text-align: center;
    font-size: 132px;
    font-weight: 700;
    letter-spacing: -2px;
    line-height: 1;
    color: var(--ink);
  }
  .byline {
    position: absolute;
    left: 0;
    width: 1200px;
    top: 205px;
    margin: 0;
    text-align: center;
    font-size: 45px;
    font-weight: 700;
    letter-spacing: 0.5px;
    line-height: 1;
    padding-left: 0;
    box-sizing: border-box;
    transform: translateX(-40px);
  }
  .byline-rule {
    position: absolute;
    left: 78px;
    top: 270px;
    width: 1070px;
    height: 6px;
    background: linear-gradient(90deg, var(--ink) 0%, var(--ink) 70%, rgba(0,0,0,0) 100%);
  }
  .credential {
    position: absolute;
    left: 66px;
    top: 288px;
    margin: 0;
    font-size: 26.5px;
    font-weight: 400;
    line-height: 1;
  }
  .mascot {
    position: absolute;
    left: 40px;
    top: 376px;
    width: 272px;
    height: 294px;
    border-radius: 46% 46% 30% 30%;
    background: var(--silhouette-tone);
  }
  .contact {
    position: absolute;
    right: 80px;
    top: 455px;
    text-align: right;
  }
  .contact-name {
    margin: 0 0 40px;
    font-size: 42px;
    font-weight: 400;
    line-height: 1;
  }
  .contact-line {
    margin: 0 0 14px;
    font-size: 30px;
    font-weight: 400;
    line-height: 1;
  }
</style>
</head>
<body>
  <main class="card">
    <svg class="card-backdrop" viewBox="0 0 1200 720" aria-hidden="true">
      <defs>
        <linearGradient id="sky-wash" x1="0" y1="0" x2="1" y2="0">
          <stop offset="0" stop-color="#ffffff"/>
          <stop offset="0.45" stop-color="#ffffff"/>
          <stop offset="0.75" stop-color="#bfe3f5"/>
          <stop offset="1" stop-color="#2aa8e0"/>
        </linearGradient>
        <linearGradient id="sky-sweep" x1="0" y1="0" x2="1" y2="1">
          <stop offset="0" stop-color="#2aa8e0"/>
          <stop offset="0.6" stop-color="#85cae6"/>
          <stop offset="1" stop-color="#d8eef9"/>
        </linearGradient>
        <linearGradient id="pale-glow" x1="0" y1="0" x2="0" y2="1">
          <stop offset="0" stop-color="#ffffff" stop-opacity="0.85"/>
          <stop offset="1" stop-color="#ffffff" stop-opacity="0.3"/>
        </linearGradient>
      </defs>
      <rect width="1200" height="720" fill="url(#sky-wash)"/>
      <path d="M640 0 H1200 V720 H1120 C1190 520 1170 300 1060 200 C950 100 780 60 640 0 Z" fill="url(#sky-sweep)" opacity="0.85"/>
      <path d="M700 60 C860 90 1010 170 1080 300 C1140 420 1130 580 1090 720 H860 C980 560 990 380 900 250 C840 160 760 100 700 60 Z" fill="url(#pale-glow)"/>
    </svg>

    <h1 class="brand-name">Brisk Hounds</h1>
    <p class="byline">“happy owners" to "Happy Owners"</p>
    <div class="byline-rule"></div>
    <p class="credential">Qualified Dog Behavioural Trainer and Natural Animal Healthcare Consultant</p>

    <div class="mascot" role="img" aria-label="Black silhouette of a sitting puppy looking upward"></div>

    <address class="contact" style="font-style: normal;">
      <p class="contact-name">Renata Walcott</p>
      <p class="contact-line">0472 680351</p>
      <p class="contact-line">briskhounds7@mailnest.example</p>
      <p class="contact-line">www.briskhounds7.example</p>
    </address>
  </main>
</body>
</html>
```